Tranquil Pathway Business Card

Logo attached. (will be printing onto thick white/off white textured card)

Double sided business card for two Therapists working at Tranquil Pathway.

Require one design, but with different name and mobile numbers on each card.

Target Market(s)

Medical, Health

Industry/Entity Type

Business

Contact Information for Business Card

Need one business card design, but a separate card for each person - Colin Marchetti and Marieke de Boeckx.

FRONT OF CARD

Logo

Name (Colin Marchetti on one card, Marieke de Boeckx on the other)
Professional Clinical Hypnotherapist

Consulting Rooms (Near Lindqvist Hospital)
482 Brackenfield Road
Dunmore VIC 3987

Colin@TranquilPathway.example.au OR Marieke@TranquilPathway.example.au

Mobile: 0455 872 604 (for Colin) OR
Mobile: 0467 290 518 (for Marieke)

BACK OF CARD

Logo

Website: www.TranquilPathway.example.au

Phone: 1300 958 471

Requirements
Must have
• Text and logo only. No additiional graphics.

```html
<!DOCTYPE html>
<html lang="en">
<head>
<meta charset="utf-8">
<title>Tranquil Pathway Business Card</title>
<link href="https://fonts.googleapis.com/css2?family=Open+Sans:wght@400;600;700&display=swap" rel="stylesheet">
<style>
  :root {
    --navy: #1f2a6e;
    --grey: #6b6c70;
    --ring: #8a8b8e;
    --card: #fbfbfb;
    --stage: #e9e9eb;
    --line: #c9cacd;
  }
  * { box-sizing: border-box; margin: 0; padding: 0; }
  html, body { width: 1200px; height: 1024px; overflow: hidden; }
  body {
    background: var(--stage);
    font-family: "Open Sans", Arial, sans-serif;
    position: relative;
  }
  .card {
    position: absolute;
    top: 162px;
    width: 400px;
    height: 700px;
    background: linear-gradient(160deg, #ffffff 0%, var(--card) 60%, #f0f0f1 100%);
    box-shadow: 0 6px 18px rgba(0,0,0,0.15);
  }
  .card--front { left: 160px; }
  .card--back { left: 640px; border-left: 8px solid var(--navy); }

  .brand {
    position: absolute;
    left: 0; right: 0;
    display: flex;
    align-items: center;
    justify-content: center;
    gap: 14px;
  }
  .brand__dot {
    width: 54px; height: 54px;
    border-radius: 50%;
    background: var(--navy);
    flex: none;
  }
  .brand__name {
    font-weight: 700;
    font-size: 26px;
    color: var(--navy);
    letter-spacing: 0.5px;
  }
  .card--front .brand { top: 150px; }
  .card--back .brand { top: 190px; }

  .divider {
    position: absolute;
    left: 30px; right: 30px;
    height: 1px;
    background: linear-gradient(90deg, transparent, var(--line) 20%, var(--line) 80%, transparent);
  }
  .card--front .divider { top: 340px; }
  .card--back .divider { top: 330px; }

  .contact {
    position: absolute;
    left: 50px; top: 380px; right: 30px;
    color: var(--grey);
  }
  .contact__name { font-size: 27px; font-weight: 700; color: var(--navy); line-height: 1.2; }
  .contact__title { font-size: 14px; margin-top: 4px; }
  .contact__rooms { font-size: 16px; font-weight: 700; color: var(--navy); margin-top: 32px; }
  .contact__near { font-size: 14px; color: var(--navy); }
  .contact__list { list-style: none; margin-top: 14px; font-size: 14px; line-height: 1.7; }
  .contact__list li { display: flex; align-items: flex-start; gap: 12px; }
  .contact__icon { width: 14px; height: 14px; flex: none; margin-top: 5px; fill: var(--navy); }
  .contact__list .indent { padding-left: 26px; }

  .web {
    position: absolute;
    left: 0; right: 0; top: 380px;
    text-align: center;
    color: var(--navy);
  }
  .web__url { font-size: 17px; font-weight: 600; }
  .web__phone { font-size: 34px; font-weight: 700; margin-top: 30px; letter-spacing: 1px; }
</style>
</head>
<body>
  <section class="card card--front" aria-label="Card front">
    <div class="brand">
      <span class="brand__dot"></span>
      <span class="brand__name">Tranquil Pathway</span>
    </div>
    <div class="divider"></div>
    <div class="contact">
      <p class="contact__name">Colin Marchetti</p>
      <p class="contact__title">Professional Clinical Hypnotherapist</p>
      <p class="contact__rooms">Consulting Rooms</p>
      <p class="contact__near">(Near Lindqvist Hospital)</p>
      <ul class="contact__list">
        <li>
          <svg class="contact__icon" viewBox="0 0 14 14"><path d="M7 0a5 5 0 0 0-5 5c0 3.5 5 9 5 9s5-5.5 5-9a5 5 0 0 0-5-5zm0 7a2 2 0 1 1 0-4 2 2 0 0 1 0 4z"/></svg>
          <span>482 Brackenfield Road</span>
        </li>
        <li class="indent">Dunmore VIC 3987</li>
        <li>
          <svg class="contact__icon" viewBox="0 0 14 14"><path d="M0 3h14v9H0zM1.5 4.2v.4L7 8.3l5.5-3.7v-.4z"/></svg>
          <span>Colin@TranquilPathway.example.au</span>
        </li>
        <li>
          <svg class="contact__icon" viewBox="0 0 14 14"><path d="M4 0h6a1 1 0 0 1 1 1v12a1 1 0 0 1-1 1H4a1 1 0 0 1-1-1V1a1 1 0 0 1 1-1zm.5 1.5v9.5h5V1.5z"/></svg>
          <span>0455 872 604</span>
        </li>
      </ul>
    </div>
  </section>

  <section class="card card--back" aria-label="Card back">
    <div class="brand">
      <span class="brand__dot"></span>
      <span class="brand__name">Tranquil Pathway</span>
    </div>
    <div class="divider"></div>
    <div class="web">
      <p class="web__url">www.TranquilPathway.example.au</p>
      <p class="web__phone">1300 958 471</p>
    </div>
  </section>
</body>
</html>
```